The Ladder of Mastery Customized for my Business

Hi! I am interested in getting some design ideas to take this Ladder of Mastery and put a bit of branding of my business into it. Open to any and all designs, this is intended to put on a 20"x24" or 16"x20" canvas so I can have it in my office for team training purposes. I have included a picture of the wall this canvas will go on. Thank you!

```html
<!DOCTYPE html>
<html lang="en">
<head>
<meta charset="utf-8">
<title>The Ladder of Mastery – Millbrook Health</title>
<link href="https://fonts.googleapis.com/css2?family=Ubuntu:wght@400;500;700&display=swap" rel="stylesheet">
<style>
  :root {
    --sky: #29abe2;
    --pyramid: #444446;
    --ink: #231f20;
    --white: #ffffff;
    --line: #1a1a1a;
  }
  * { box-sizing: border-box; margin: 0; padding: 0; }
  html, body { width: 1000px; height: 1200px; overflow: hidden; background: var(--white); }
  body { font-family: "Ubuntu", sans-serif; color: var(--ink); }
  .poster { position: relative; width: 1000px; height: 1200px; }
  .poster__art { position: absolute; inset: 0; }

  .brand {
    position: absolute; left: 445px; top: 186px; width: 110px; height: 110px;
    border-radius: 50%; background: var(--ink); border: 3px solid var(--white);
    display: flex; align-items: center; justify-content: center;
  }
  .brand__name { color: var(--white); font-weight: 700; font-size: 17px; }

  .block {
    position: absolute; width: 131px; height: 93px; border-radius: 50%;
    overflow: hidden; border: 1px solid var(--white); background: var(--ink);
    transform: translateX(-50%); display: flex; flex-direction: column;
  }
  .block__title {
    height: 32px; flex: none; background: var(--sky); color: var(--ink);
    font-weight: 500; font-size: 10.5px; line-height: 11px;
    display: flex; align-items: flex-end; justify-content: center;
    text-align: center; padding-bottom: 3px;
  }
  .block__text {
    color: var(--white); font-size: 6.6px; line-height: 8.4px; font-weight: 500;
    text-align: center; padding: 8px 14px 0;
  }

  .trait { position: absolute; width: 170px; transform: translateX(-50%); text-align: center; }
  .trait__icon {
    display: block; margin: 0 auto 3px; width: 30px; height: 30px; border-radius: 6px;
    background: linear-gradient(135deg, var(--ink) 55%, var(--sky));
  }
  .trait__name { font-weight: 700; font-size: 14px; line-height: 15px; }
  .trait__note { font-size: 9.5px; line-height: 12px; }

  .title-band {
    position: absolute; left: 71px; top: 837px; width: 858px; height: 101px;
    border-radius: 51px; background: var(--sky); border: 6px solid var(--pyramid);
    display: flex; align-items: center; justify-content: center;
  }
  .title-band__text { font-weight: 700; font-size: 63px; letter-spacing: -2px; color: var(--ink); white-space: nowrap; }

  .web {
    position: absolute; left: 280px; top: 1133px; width: 439px; height: 44px;
    border-radius: 22px; background: var(--sky); color: var(--white);
    font-size: 20px; display: flex; align-items: center; justify-content: center;
  }
</style>
</head>
<body>
<main class="poster">
  <svg class="poster__art" width="1000" height="1200" viewBox="0 0 1000 1200" aria-hidden="true">
    <polygon points="500,262 74,895 926,895" fill="var(--pyramid)"/>
    <g stroke="var(--line)" stroke-width="1.5" fill="none">
      <polyline points="310,311 440,311 460,282"/>
      <polyline points="240,413 370,413 434,320"/>
      <polyline points="170,514 300,514 364,423"/>
      <polyline points="98,618 229,618 292,526"/>
      <polyline points="27,721 157,721 221,629"/>
      <polyline points="690,311 560,311 540,282"/>
      <polyline points="760,413 629,413 566,320"/>
      <polyline points="830,514 700,514 636,423"/>
      <polyline points="902,618 771,618 707,526"/>
      <polyline points="973,721 843,721 779,629"/>
    </g>
  </svg>

  <div class="brand"><span class="brand__name">Millbrook</span></div>

  <div class="block" style="left:500px;top:320px"><div class="block__title">PEAK<br>PERFORMANCE</div><p class="block__text">Rise to the moment when it matters most. Find joy in a hard task.</p></div>

  <div class="block" style="left:431px;top:423px"><div class="block__title">COMPOSURE</div><p class="block__text">Stay true to who you are. Remain calm in every setting. Never doubt yourself.</p></div>
  <div class="block" style="left:569px;top:423px"><div class="block__title">SELF-BELIEF</div><p class="block__text">Trust built on preparation. Keep every task &amp; goal in its proper place.</p></div>

  <div class="block" style="left:363px;top:526px"><div class="block__title">FITNESS</div><p class="block__text">Body, mind &amp; habits. Sleep, movement &amp; nutrition all matter. Keep balance &amp; drop what drains you.</p></div>
  <div class="block" style="left:500px;top:526px"><div class="block__title">EXPERTISE</div><p class="block__text">Deep knowledge of the craft &amp; the ability to apply the basics quickly &amp; well.</p></div>
  <div class="block" style="left:637px;top:526px"><div class="block__title">UNITY</div><p class="block__text">Real care for colleagues. A readiness to put the group's success ahead of credit.</p></div>

  <div class="block" style="left:295px;top:629px"><div class="block__title">DISCIPLINE</div><p class="block__text">Hold steady under pressure &amp; keep feelings in check. Sound reasoning is vital.</p></div>
  <div class="block" style="left:431px;top:629px"><div class="block__title">AWARENESS</div><p class="block__text">Notice everything around you. Stay curious. Keep learning &amp; growing.</p></div>
  <div class="block" style="left:569px;top:629px"><div class="block__title">DRIVE</div><p class="block__text">Act without waiting to be asked. Trust your thinking. Treat mistakes as lessons.</p></div>
  <div class="block" style="left:705px;top:629px"><div class="block__title">FOCUS</div><p class="block__text">Choose a clear target. Work toward it steadily, avoid distractions &amp; stay committed.</p></div>

  <div class="block" style="left:227px;top:731px"><div class="block__title">DILIGENCE</div><p class="block__text">Effort has no shortcut. Lasting results come from steady work &amp; planning.</p></div>
  <div class="block" style="left:363px;top:731px"><div class="block__title">RAPPORT</div><p class="block__text">Built on trust, kindness &amp; shared respect. It needs care from both sides.</p></div>
  <div class="block" style="left:500px;top:731px"><div class="block__title">DEPENDABILITY</div><p class="block__text">To yourself &amp; everyone who counts on you. Keep your word &amp; standards.</p></div>
  <div class="block" style="left:637px;top:731px"><div class="block__title">COLLABORATION</div><p class="block__text">Across every role. Listen first to be heard. Seek the best answer, not your own.</p></div>
  <div class="block" style="left:773px;top:731px"><div class="block__title">ENERGY</div><p class="block__text">Spreads to everyone around you. Love what you do &amp; let it show.</p></div>

  <div class="trait" style="left:390px;top:239px"><span class="trait__icon" role="img" aria-label="Compass icon"></span><p class="trait__name">Purpose</p><p class="trait__note">(a clear why)</p></div>
  <div class="trait" style="left:315px;top:342px"><span class="trait__icon" role="img" aria-label="Raised arms icon"></span><p class="trait__name">Grit</p><p class="trait__note">(steady effort)</p></div>
  <div class="trait" style="left:241px;top:444px"><span class="trait__icon" role="img" aria-label="Lightbulb icon"></span><p class="trait__name">Ingenuity</p><p class="trait__note">(sound choices)</p></div>
  <div class="trait" style="left:171px;top:548px"><span class="trait__icon" role="img" aria-label="Circular arrows icon"></span><p class="trait__name">Flexibility</p><p class="trait__note">(in any setting)</p></div>
  <div class="trait" style="left:101px;top:651px"><span class="trait__icon" role="img" aria-label="Horizon icon"></span><p class="trait__name">Vision</p><p class="trait__note">(for worthy aims)</p></div>

  <div class="trait" style="left:618px;top:239px"><span class="trait__icon" role="img" aria-label="Hourglass icon"></span><p class="trait__name">Persistence</p><p class="trait__note">(progress takes time)</p></div>
  <div class="trait" style="left:682px;top:342px"><span class="trait__icon" role="img" aria-label="Shield icon"></span><p class="trait__name">Character</p><p class="trait__note">(pure motives)</p></div>
  <div class="trait" style="left:753px;top:444px"><span class="trait__icon" role="img" aria-label="Thumbs up icon"></span><p class="trait__name">Consistency</p><p class="trait__note">(earns trust)</p></div>
  <div class="trait" style="left:827px;top:548px"><span class="trait__icon" role="img" aria-label="Speech bubble icon"></span><p class="trait__name">Candor</p><p class="trait__note">(in word and deed)</p></div>
  <div class="trait" style="left:892px;top:651px"><span class="trait__icon" role="img" aria-label="Heart icon"></span><p class="trait__name">Warmth</p><p class="trait__note">(builds bonds)</p></div>

  <div class="title-band"><h1 class="title-band__text">THE LADDER OF MASTERY</h1></div>

  <p class="web">www.millbrookhealth.com</p>
</main>
</body>
</html>
```